Travel Blogger Business Card for wanderquill.net

I need a two-sided business card for a travel blogging website. The card should be both professional and fun at the same time. This is for the website www.wanderquill.net

I don't necessarily think that the current logo on the website needs to be used on the business card but it can be. I am very flexible with ideas

Target Market(s)

Travel agencies that will be met at a conference.

Industry/Entity Type

Travel

Contact Information for Business Card

Company Name: Wander Quill.net
Name: Marcel Vennor
Voice: +1-(345)-555-0193
Address: Coral Reed Shore, Grand Cayman, Cayman Islands
Email: ceo@wanderquill.net

Colors
0592cd
0355a3
3176b5
33a6d7
85cae6
85acd3

Requirements
Must have
• Website address and name should be bigger than address, phone number, and email.

```html
<!DOCTYPE html>
<html lang="en">
<head>
<meta charset="utf-8">
<title>Wander Quill – Business Card</title>
<link rel="stylesheet" href="https://fonts.googleapis.com/css2?family=Cabin:wght@400;700&family=Roboto:wght@300&display=swap">
<style>
  :root {
    --page: #ffffff;
    --label: #a9a9a9;
    --card: #0355a3;
    --ink: #ffffff;
    --pillar: #85cae6;
    --rule: #85acd3;
    --icon: #0355a3;
  }
  * { box-sizing: border-box; margin: 0; padding: 0; }
  html, body { width: 1200px; height: 467px; overflow: hidden; background: var(--page); }
  body { position: relative; font-family: "Cabin", sans-serif; color: var(--ink); }

  .side-label {
    position: absolute; top: 56px; width: 499px; text-align: center;
    font-family: "Roboto", sans-serif; font-weight: 300; font-size: 26px;
    color: var(--label); letter-spacing: 1px;
  }
  .side-label--front { left: 73px; }
  .side-label--back { left: 628px; }

  .card {
    position: absolute; top: 106px; width: 499px; height: 300px;
    background: var(--card); overflow: hidden;
  }
  .card--front { left: 73px; }
  .card--back { left: 628px; }

  .brand { position: absolute; display: flex; align-items: center; white-space: nowrap; }
  .brand__dot { background: var(--ink); border-radius: 50%; flex: none; }
  .brand__name { font-weight: 700; color: var(--ink); letter-spacing: 0.3px; }

  .card--front .brand { left: 266px; top: 54px; gap: 10px; }
  .card--front .brand__dot { width: 22px; height: 22px; }
  .card--front .brand__name { font-size: 21px; }

  .holder {
    position: absolute; left: 66px; top: 132px;
    font-size: 26px; font-weight: 400; line-height: 1;
    padding-bottom: 3px; border-bottom: 1px solid var(--rule);
  }

  .pillar { position: absolute; top: 195px; width: 26px; height: 105px; }
  .pillar--left { left: 66px; }
  .pillar--right { left: 270px; }
  .pillar__seg { position: absolute; left: 0; width: 26px; background: var(--pillar); display: flex; align-items: center; justify-content: center; }
  .pillar__seg--top { top: 0; height: 30px; border-radius: 13px 13px 0 0; padding-top: 4px; }
  .pillar__seg--mid { top: 33px; height: 27px; }
  .pillar__seg--base { top: 63px; height: 42px; }
  .pillar svg { width: 14px; height: 14px; fill: var(--icon); }

  .contact { position: absolute; font-size: 12px; line-height: 15px; white-space: nowrap; }
  .contact--phone { left: 106px; top: 204px; }
  .contact--address { left: 106px; top: 233px; }
  .contact--email { left: 307px; top: 204px; }
  .contact--web { left: 311px; top: 234px; }

  .card--back .brand { left: 0; right: 0; top: 128px; justify-content: center; gap: 16px; }
  .card--back .brand__dot { width: 40px; height: 40px; }
  .card--back .brand__name { font-size: 34px; }
  .back-url {
    position: absolute; left: 0; right: 0; top: 226px; text-align: center;
    font-size: 11px; letter-spacing: 5.4px;
  }
</style>
</head>
<body>
  <div class="side-label side-label--front">FRONT</div>
  <div class="side-label side-label--back">BACK</div>

  <section class="card card--front">
    <div class="brand">
      <span class="brand__dot"></span>
      <span class="brand__name">WANDER QUILL</span>
    </div>

    <h1 class="holder">Marcel Vennor</h1>

    <div class="pillar pillar--left">
      <div class="pillar__seg pillar__seg--top">
        <svg viewBox="0 0 24 24" aria-hidden="true"><path d="M6.6 10.8a15.1 15.1 0 0 0 6.6 6.6l2.2-2.2c.3-.3.7-.4 1-.2 1.1.4 2.3.6 3.6.6.6 0 1 .4 1 1V20c0 .6-.4 1-1 1A17 17 0 0 1 3 4c0-.6.4-1 1-1h3.5c.6 0 1 .4 1 1 0 1.3.2 2.5.6 3.6.1.3 0 .7-.2 1z"/></svg>
      </div>
      <div class="pillar__seg pillar__seg--mid">
        <svg viewBox="0 0 24 24" aria-hidden="true"><path d="M12 2a7 7 0 0 0-7 7c0 5.2 7 13 7 13s7-7.8 7-13a7 7 0 0 0-7-7zm0 9.5A2.5 2.5 0 1 1 12 6.5a2.5 2.5 0 0 1 0 5z"/></svg>
      </div>
      <div class="pillar__seg pillar__seg--base"></div>
    </div>

    <div class="pillar pillar--right">
      <div class="pillar__seg pillar__seg--top">
        <svg viewBox="0 0 24 24" aria-hidden="true"><path d="M3 5h18v14H3zm2 2v.4l7 4.6 7-4.6V7zm0 2.8V17h14V9.8l-7 4.6z"/></svg>
      </div>
      <div class="pillar__seg pillar__seg--mid">
        <svg viewBox="0 0 24 24" aria-hidden="true"><path d="M12 2a10 10 0 1 0 0 20 10 10 0 0 0 0-20zm6.9 6h-2.9a15.7 15.7 0 0 0-1.4-3.6A8 8 0 0 1 18.9 8zM12 4c.8 1.2 1.5 2.5 1.9 4h-3.8c.4-1.4 1.1-2.8 1.9-4zM4.3 14a8.2 8.2 0 0 1 0-4h3.4a16.5 16.5 0 0 0 0 4zm.8 2h2.9c.3 1.3.8 2.5 1.4 3.6A8 8 0 0 1 5.1 16zM8 8H5.1a8 8 0 0 1 4.3-3.6C8.8 5.5 8.3 6.7 8 8zm4 12c-.8-1.2-1.5-2.5-1.9-4h3.8c-.4 1.4-1.1 2.8-1.9 4zm2.3-6H9.7a14.7 14.7 0 0 1 0-4h4.6a14.7 14.7 0 0 1 0 4zm.3 5.6c.6-1.1 1.1-2.3 1.4-3.6h2.9a8 8 0 0 1-4.3 3.6zm1.7-5.6a16.5 16.5 0 0 0 0-4h3.4a8.2 8.2 0 0 1 0 4z"/></svg>
      </div>
      <div class="pillar__seg pillar__seg--base"></div>
    </div>

    <p class="contact contact--phone">+1-(345)-555-0193</p>
    <p class="contact contact--address">Coral Reed Shore, Grand<br>Cayman, Cayman Islands</p>
    <p class="contact contact--email">ceo@wanderquill.net</p>
    <p class="contact contact--web">www.wanderquill.net</p>
  </section>

  <section class="card card--back">
    <div class="brand">
      <span class="brand__dot"></span>
      <span class="brand__name">WANDER QUILL</span>
    </div>
    <p class="back-url">www.wanderquill.net</p>
  </section>
</body>
</html>
```